Online media outlet needs a blog and logo

A new online blog platform is being established in the UK. The blog will be very similar in layout to www.dravonet.co. It will need to have a main story slider showing three slides and block tiles beneath the slider for additional tiles.

The blog platform will be called 'Tarsel Quill' and will also need a professional looking logo design for the name.

The website should be designed in Word Press.

Industry/Entity Type

Media

Logo Text

Tarsel Quill

Coding

Coded - Design and coding required

Number of Pages Required

3 page

Font styles to use
Other font styles liked:
• Helvetica

Requirements
Must have
• A slider showing three slides. Be similar to Drav N (see previous comment). Be Word Press compatible.

```html
<!DOCTYPE html>
<html lang="en">
<head>
<meta charset="utf-8">
<title>Tarsel Quill</title>
<link href="https://fonts.googleapis.com/css2?family=Open+Sans:wght@400;600;700;800&display=swap" rel="stylesheet">
<style>
:root{
  --red:#e3200f;
  --dark:#1c1c1c;
  --footer:#262626;
  --ink:#222;
  --muted:#666;
  --grey-bg:#efefef;
  --white:#fff;
}
*{box-sizing:border-box;margin:0;padding:0}
html,body{width:1200px;height:3614px;overflow:hidden}
body{font-family:"Open Sans",Helvetica,Arial,sans-serif;color:var(--ink);background:var(--white);position:relative}

/* header */
.topbar{position:absolute;top:0;left:0;width:1200px;height:72px;background:var(--dark)}
.brand{position:absolute;left:161px;top:24px;font-weight:800;font-size:20px;color:var(--white);letter-spacing:.2px}
.nav{position:absolute;top:29px;left:400px;display:flex;gap:26px;align-items:center}
.nav a{white-space:nowrap;color:#ddd;font-size:11px;font-weight:600;text-decoration:none;letter-spacing:.2px}
.search{position:absolute;left:867px;top:22px;width:169px;height:28px;background:var(--white);border-radius:2px}
.search svg{position:absolute;right:8px;top:7px}

/* hero */
.hero{position:absolute;top:72px;left:0;width:1200px;height:497px;overflow:hidden;background:linear-gradient(160deg,#6e6a6a 0%,#4a4545 45%,#2c2a2c 100%)}
.hero::after{content:"";position:absolute;inset:0;background:linear-gradient(180deg,rgba(0,0,0,0) 40%,rgba(0,0,0,.55) 100%)}
.hero-text{position:absolute;left:161px;top:309px;z-index:1;color:var(--white)}
.badge{display:inline-flex;align-items:center;gap:6px;background:var(--red);color:var(--white);font-size:11px;font-weight:700;padding:4px 9px}
.hero-title{font-size:31px;font-weight:700;line-height:40px;margin-top:14px;width:640px}
.hero-sub{font-size:13px;margin-top:8px;color:#eee}
.dots{position:absolute;left:971px;top:443px;display:flex;gap:4px;z-index:2}
.dots span{width:14px;height:10px;background:var(--white)}
.dots span.active{background:var(--red)}

/* sections */
.section{position:absolute;left:0;width:1200px}
.grey{background:var(--grey-bg)}
.sec-head{position:absolute;left:161px;width:878px;display:flex;justify-content:space-between;align-items:center}
.sec-head h2{font-size:21px;font-weight:600;color:var(--ink);border-left:4px solid var(--red);padding-left:9px;line-height:22px}
.sec-head .aside{color:var(--red);font-size:14px;font-weight:600}

/* tiles */
.tile{position:absolute;overflow:hidden}
.tile .ph{position:absolute;inset:0}
.tile .cap{position:absolute;left:0;right:0;bottom:0;padding:0 30px 22px;color:var(--white);background:linear-gradient(180deg,rgba(0,0,0,0),rgba(0,0,0,.6))}
.tile.small .cap{padding:0 18px 16px}
.cap h3{font-size:19px;font-weight:600;line-height:24px}
.tile.small .cap h3{font-size:14px;line-height:18px}
.cap p{font-size:11px;line-height:16px;margin-top:8px;color:#eee}
.cap .date{display:flex;align-items:center;gap:5px;font-size:10px;font-weight:700;margin-top:8px}
.tile.red{background:var(--red);color:var(--white);padding:16px 18px}
.tile.red h3{font-size:14px;line-height:18px;font-weight:600}
.tile.red p{font-size:10.5px;line-height:15px;margin-top:8px}
.tile.red .date{display:flex;align-items:center;gap:5px;font-size:10px;font-weight:700;position:absolute;bottom:16px;left:18px}

/* cards */
.cards{position:absolute;left:161px;width:878px;display:grid;grid-template-columns:278px 278px 278px;column-gap:22px}
.card .ph{height:159px}
.card .date{display:flex;align-items:center;gap:5px;color:var(--red);font-size:10px;font-weight:700;margin-top:17px}
.card h3{font-size:18px;font-weight:600;margin-top:12px;color:var(--ink)}
.card p{font-size:11px;line-height:15px;color:var(--muted);margin-top:10px;width:270px}
.btn{display:inline-block;background:var(--red);color:var(--white);font-size:10px;font-weight:700;padding:7px 13px;margin-top:15px}

/* footer */
.footer{position:absolute;top:3307px;left:0;width:1200px;height:307px;background:var(--footer);border-top:5px solid var(--red)}
.foot-brand{position:absolute;left:161px;top:32px;font-weight:800;font-size:21px;color:var(--white)}
.social{position:absolute;left:884px;top:32px;display:flex;gap:8px}
.social span{width:23px;height:23px;border:1px solid #bbb;border-radius:50%}
.cols{position:absolute;left:161px;top:91px;width:878px;display:grid;grid-template-columns:repeat(5,1fr)}
.cols ul{list-style:none;border-left:1px solid #444;padding:0 0 0 30px;height:121px}
.cols ul:first-child{border-left:none;padding-left:0}
.cols li{font-size:11px;line-height:19.5px;color:#ccc}
.foot-rule{position:absolute;left:161px;top:240px;width:878px;height:1px;background:#444}
.copy{position:absolute;left:0;width:1200px;top:270px;text-align:center;font-size:10.5px;color:#ccc}
</style>
</head>
<body>

<header class="topbar">
  <div class="brand">TARSEL QUILL</div>
  <nav class="nav">
    <a>NEWS</a>
    <a>ABOUT TARSEL QUILL</a>
    <a>ALL TOPICS</a>
    <a>SPECIAL NEWS</a>
    <a>MORE &#9662;</a>
  </nav>
  <div class="search"><svg width="14" height="14" viewBox="0 0 14 14"><circle cx="6" cy="6" r="4.2" fill="none" stroke="#222" stroke-width="1.8"/><line x1="9" y1="9" x2="13" y2="13" stroke="#222" stroke-width="1.8"/></svg></div>
</header>

<section class="hero" role="img" aria-label="Photo of a busy city street with pedestrians, a woman walking in the foreground">
  <div class="hero-text">
    <span class="badge"><svg width="10" height="10" viewBox="0 0 10 10"><rect x="1" y="2" width="8" height="7" fill="none" stroke="#fff"/><line x1="1" y1="4" x2="9" y2="4" stroke="#fff"/></svg>MAY 04 2016</span>
    <div class="hero-title">Sed ut perspiciatis unde omnis iste natussitedut perspiciatis unde</div>
    <div class="hero-sub">Sed ut perspiciatis unde omnis iste natus error sit voluptatem</div>
  </div>
  <div class="dots"><span class="active"></span><span></span><span></span></div>
</section>

<!-- welcome -->
<section class="section grey" style="top:569px;height:448px">
  <div class="sec-head" style="top:25px"><h2>Welcome to Tarsel Quill</h2><span class="aside">Wednesday, 4 May</span></div>
  <div class="tile" style="left:161px;top:72px;width:432px;height:313px">
    <div class="ph" role="img" aria-label="Photo of colleagues discussing work at a laptop" style="background:linear-gradient(135deg,#8a9aa6,#4e5a62)"></div>
    <div class="cap"><h3>Sed ut perspiciatis unde omnis istenatu</h3><p>Sed ut perspiciatis unde omnis iste natus error sit voluptatem accusantium doloremque laudantium, totam rem aperiam, eaque ipsa quae ab illo</p><div class="date">&#9633; MAY 04 2016</div></div>
  </div>
  <div class="tile red" style="left:600px;top:72px;width:212px;height:149px">
    <h3>Sed ut perspiciatis unde omnis isteerspiciana</h3>
    <p>Sed ut perspiciatis unde omnis iste natus error sit voluptatem accus ant ium doloremque laudant</p>
    <div class="date">&#9633; MAY 04 2016</div>
  </div>
  <div class="tile small" style="left:822px;top:72px;width:217px;height:149px">
    <div class="ph" role="img" aria-label="Photo of a tablet on a desk" style="background:linear-gradient(135deg,#a7a9ad,#5e6266)"></div>
    <div class="cap"><h3>Sed ut perspiciatis unde omnis isteerspiciana</h3></div>
  </div>
  <div class="tile small" style="left:600px;top:231px;width:212px;height:154px">
    <div class="ph" role="img" aria-label="Photo of a businessman at work" style="background:linear-gradient(135deg,#7a7470,#3b3634)"></div>
    <div class="cap"><h3>Sed ut perspiciatis unde omnis isteerspiciana</h3><div class="date">&#9633; MAY 04 2016</div></div>
  </div>
  <div class="tile small" style="left:822px;top:231px;width:217px;height:154px">
    <div class="ph" role="img" aria-label="Photo of hands holding a phone" style="background:linear-gradient(135deg,#a07a62,#4a362a)"></div>
    <div class="cap"><h3>Sed ut perspiciatis unde omnis isteerspiciana</h3><div class="date">&#9633; MAY 04 2016</div></div>
  </div>
</section>

<!-- blog -->
<section class="section" style="top:1017px;height:439px">
  <div class="sec-head" style="top:28px"><h2>Latest Blog News</h2></div>
  <div class="cards" style="top:80px">
    <article class="card"><div class="ph" role="img" aria-label="Photo of a team gathered around a laptop" style="background:linear-gradient(135deg,#c9a996,#7a6458)"></div><div class="date">&#9633; MAY 04 2016</div><h3>Sed ut perspiciatis undemnis</h3><p>Sed ut perspiciatis unde omnis iste natus error sit voluptatem accusantium doloremque laudantium, totam rem aperiam, eaque ipsa quae ab illoed ut</p><span class="btn">READ MORE</span></article>
    <article class="card"><div class="ph" role="img" aria-label="Photo of a desk with glasses and a sketchbook" style="background:linear-gradient(135deg,#c9874f,#6b4630)"></div><div class="date">&#9633; MAY 04 2016</div><h3>Sed ut perspiciatis undemnis</h3><p>Sed ut perspiciatis unde omnis iste natus error sit voluptatem accusantium doloremque laudantium, totam rem aperiam, eaque ipsa quae ab illoed ut</p><span class="btn">READ MORE</span></article>
    <article class="card"><div class="ph" role="img" aria-label="Photo of a laptop and phone on a grey desk" style="background:linear-gradient(135deg,#8c8c8c,#4a4a4a)"></div><div class="date">&#9633; MAY 04 2016</div><h3>Sed ut perspiciatis undemnis</h3><p>Sed ut perspiciatis unde omnis iste natus error sit voluptatem accusantium doloremque laudantium, totam rem aperiam, eaque ipsa quae ab illoed ut</p><span class="btn">READ MORE</span></article>
  </div>
</section>

<!-- business -->
<section class="section grey" style="top:1456px;height:484px">
  <div class="sec-head" style="top:30px"><h2>Latest Business News</h2><span class="aside">View More News</span></div>
  <div class="tile" style="left:161px;top:69px;width:591px;height:362px">
    <div class="ph" role="img" aria-label="Photo of a business meeting around a table" style="background:linear-gradient(135deg,#9aa3a5,#4d5456)"></div>
    <div class="cap"><h3>Sed ut perspiciatis unde omnis istenatu</h3><p>Sed ut perspiciatis unde omnis iste natus error sit voluptatem accusantium doloremque laudantium, totam rem aperiam, eaque ipsa quae ab illo</p><div class="date">&#9633; MAY 04 2016</div></div>
  </div>
  <div class="tile small" style="left:762px;top:69px;width:277px;height:176px">
    <div class="ph" role="img" aria-label="Photo of hands using tablets on a table" style="background:linear-gradient(135deg,#6f8a8c,#3a4446)"></div>
    <div class="cap"><h3>Sed ut perspiciatis unde omnis ister spicianarspiciatis unpiciatis.</h3><div class="date">&#9633; MAY 04 2016</div></div>
  </div>
  <div class="tile small" style="left:762px;top:255px;width:277px;height:176px">
    <div class="ph" role="img" aria-label="Photo of a woman using a tablet" style="background:linear-gradient(135deg,#a8765a,#4a3224)"></div>
    <div class="cap"><h3>Sed ut perspiciatis unde omnis ister spicianarspiciatis unpiciatis.</h3><div class="date">&#9633; MAY 04 2016</div></div>
  </div>
</section>

<!-- more -->
<section class="section" style="top:1940px;height:434px">
  <div class="sec-head" style="top:25px"><h2>More from around the Tarsel Quill</h2></div>
  <div class="cards" style="top:72px">
    <article class="card"><div class="ph" role="img" aria-label="Photo of a smartphone on a table" style="background:linear-gradient(135deg,#8a8783,#3e3c3a)"></div><div class="date">&#9633; MAY 04 2016</div><h3>Sed ut perspiciatis undemnis</h3><p>Sed ut perspiciatis unde omnis iste natus error sit voluptatem accusantium doloremque laudantium, totam rem aperiam, eaque ipsa quae ab illoed ut</p><span class="btn">READ MORE</span></article>
    <article class="card"><div class="ph" role="img" aria-label="Illustration of app icons bursting from a phone" style="background:radial-gradient(circle at 60% 40%,#b88a3a,#1e1e22 70%)"></div><div class="date">&#9633; MAY 04 2016</div><h3>Sed ut perspiciatis undemnis</h3><p>Sed ut perspiciatis unde omnis iste natus error sit voluptatem accusantium doloremque laudantium, totam rem aperiam, eaque ipsa quae ab illoed ut</p><span class="btn">READ MORE</span></article>
    <article class="card"><div class="ph" role="img" aria-label="Photo of a woman with a tablet in warm sunlight" style="background:linear-gradient(135deg,#f0b040,#a0561e)"></div><div class="date">&#9633; MAY 04 2016</div><h3>Sed ut perspiciatis undemnis</h3><p>Sed ut perspiciatis unde omnis iste natus error sit voluptatem accusantium doloremque laudantium, totam rem aperiam, eaque ipsa quae ab illoed ut</p><span class="btn">READ MORE</span></article>
  </div>
</section>

<!-- media -->
<section class="section grey" style="top:2374px;height:487px">
  <div class="sec-head" style="top:27px"><h2>Media News</h2><span class="aside">View More News</span></div>
  <div class="tile" style="left:161px;top:72px;width:589px;height:362px">
    <div class="ph" role="img" aria-label="Photo of a hand holding a smartphone" style="background:linear-gradient(135deg,#7c9a8e,#3c4442)"></div>
    <div class="cap"><h3>Sed ut perspiciatis unde omnis istenatu</h3><p>Sed ut perspiciatis unde omnis iste natus error sit voluptatem accusantium doloremque laudantium, totam rem aperiam, eaque ipsa quae ab illo</p><div class="date">&#9633; MAY 04 2016</div></div>
  </div>
  <div class="tile small" style="left:759px;top:72px;width:280px;height:174px">
    <div class="ph" role="img" aria-label="Photo of friends looking at phones" style="background:linear-gradient(135deg,#a09a88,#4a463c)"></div>
    <div class="cap"><h3>Sed ut perspiciatis unde omnis ister spicianarspiciatis unpiciatis.</h3><div class="date">&#9633; MAY 04 2016</div></div>
  </div>
  <div class="tile red" style="left:759px;top:258px;width:280px;height:176px">
    <h3>Sed ut perspiciatis unde omni spicianarspiciatis unpiciatis.</h3>
    <p>Sed ut perspiciatis unde omnis iste natus er ror sit voluptatem accusantium doloremque laudantiumed ut perspiciatis unde omnl</p>
    <div class="date">&#9633; MAY 04 2016</div>
  </div>
</section>

<!-- live -->
<section class="section" style="top:2861px;height:446px">
  <div class="sec-head" style="top:37px"><h2>Live Tarsel Quill News</h2></div>
  <div class="cards" style="top:82px">
    <article class="card"><div class="ph" role="img" aria-label="Photo of a tablet with floating app icons" style="background:linear-gradient(135deg,#4aa0c8,#1e4458)"></div><div class="date">&#9633; MAY 04 2016</div><h3>Sed ut perspiciatis undemnis</h3><p>Sed ut perspiciatis unde omnis iste natus error sit voluptatem accusantium doloremque laudantium, totam rem aperiam, eaque ipsa quae ab illoed ut</p><span class="btn">READ MORE</span></article>
    <article class="card"><div class="ph" role="img" aria-label="Photo of business people looking at a screen" style="background:linear-gradient(135deg,#c8c4be,#5a5650)"></div><div class="date">&#9633; MAY 04 2016</div><h3>Sed ut perspiciatis undemnis</h3><p>Sed ut perspiciatis unde omnis iste natus error sit voluptatem accusantium doloremque laudantium, totam rem aperiam, eaque ipsa quae ab illoed ut</p><span class="btn">READ MORE</span></article>
    <article class="card"><div class="ph" role="img" aria-label="Photo of a collage of digital devices" style="background:linear-gradient(135deg,#6a7a8a,#22282e)"></div><div class="date">&#9633; MAY 04 2016</div><h3>Sed ut perspiciatis undemnis</h3><p>Sed ut perspiciatis unde omnis iste natus error sit voluptatem accusantium doloremque laudantium, totam rem aperiam, eaque ipsa quae ab illoed ut</p><span class="btn">READ MORE</span></article>
  </div>
</section>

<footer class="footer">
  <div class="foot-brand">TARSEL QUILL</div>
  <div class="social"><span></span><span></span><span></span><span></span><span></span></div>
  <div class="cols">
    <ul><li>Sed ut perspicitis</li><li>Dmnis iste natus</li><li>Wit volu ptatem</li><li>Accusantium</li><li>Doloremque</li><li>Ludantiutotam</li></ul>
    <ul><li>Sed ut perspicitis</li><li>Dmnis iste natus</li><li>Wit volu ptatem</li><li>Accusantium</li><li>Doloremque</li><li>Ludantiutotam</li></ul>
    <ul><li>Sed ut perspicitis</li><li>Dmnis iste natus</li><li>Wit volu ptatem</li><li>Accusantium</li><li>Doloremque</li><li>Ludantiutotam</li></ul>
    <ul><li>Sed ut perspicitis</li><li>Dmnis iste natus</li><li>Wit volu ptatem</li><li>Accusantium</li><li>Doloremque</li><li>Ludantiutotam</li></ul>
    <ul><li>Sed ut perspicitis</li><li>Dmnis iste natus</li><li>Wit volu ptatem</li><li>Accusantium</li><li>Doloremque</li><li>Ludantiutotam</li></ul>
  </div>
  <div class="foot-rule"></div>
  <div class="copy">© 2016 Tarsel Quill. All Copyrights are reserved &nbsp;Term of Use. Privacy Policy</div>
</footer>

</body>
</html>
```